Lawyers in the Netherlands website + logo

We are going in 2015 to launch a website where all law firms in the Netherlands and have the opportunity to place an ad program.

The domain name wil be:

kantoorvinder.website

We want a responsive PSD bootstrap twitter 1170 pixel grid.
for the homepage, result page and the detail page of the customer.

This sites we like:
https://www.qorvantis.com/lawyers

https://lawyers.qorvantis.com/lawyer/tim-garsby-7305826

http://solicitordirectory.brevimark.co.uk/
Map of the Netherlands?

http://solicitordirectory.brevimark.co.uk/listing/category-search/commercial
http://www.tandelvo.com.au/find-a-lawyer/banking-finance-law/

```html
<!DOCTYPE html>
<html lang="en">
<head>
<meta charset="utf-8">
<title>KantoorVinder – Find a Law Firm in the Netherlands</title>
<link rel="stylesheet" href="https://fonts.googleapis.com/css2?family=Fjalla+One&family=Open+Sans:wght@400;600&display=swap">
<style>
:root{
  --blue:#1fa0dd;
  --blue-dark:#1a8fc8;
  --orange:#f47a20;
  --navy:#1f3a5a;
  --text:#2d3e50;
  --grey-bg:#eef0f3;
  --grey-line:#c9ccd1;
  --white:#ffffff;
}
*{box-sizing:border-box;margin:0;padding:0}
html,body{width:1200px;height:2463px;overflow:hidden}
body{position:relative;background:var(--white);font-family:"Open Sans",Arial,sans-serif;color:var(--text)}
.abs{position:absolute}
.top-strip{left:0;top:0;width:1200px;height:4px;background:var(--grey-line)}
.brand{left:70px;top:40px}
.brand-name{font-family:"Open Sans",Arial,sans-serif;font-weight:600;font-size:36px;color:var(--blue);display:flex;align-items:center;gap:10px;line-height:1}
.brand-name .dot{width:18px;height:18px;border-radius:50%;background:var(--blue)}
.brand-tag{font-size:11px;letter-spacing:2px;color:var(--orange);margin-top:10px;margin-left:28px}
.btn{top:42px;height:30px;background:var(--orange);color:var(--white);font-size:15px;line-height:30px;text-align:center;border-radius:3px;box-shadow:0 2px 0 #b9561a}
.btn-signin{left:890px;width:66px}
.btn-listed{left:985px;width:152px}
.nav{left:0;top:121px;width:1200px;height:60px;background:var(--blue)}
.nav ul{list-style:none;display:flex;height:60px;margin-left:62px}
.nav li{color:var(--white);font-size:13px;line-height:60px;padding:0 28px;text-transform:uppercase}
.nav li.active{background:var(--orange);padding:0 14px}
.nav li:nth-child(2){padding-left:28px}
.hero{left:0;top:181px;width:1200px;height:404px;background:linear-gradient(180deg,#d7dde3 0%,#9aa4ad 45%,#6c7680 100%)}
.search-panel{left:240px;top:336px;width:696px;height:160px;background:rgba(255,255,255,.12);border:1px solid rgba(255,255,255,.3)}
.search-title{left:240px;top:340px;width:696px;text-align:center;font-family:"Fjalla One",Arial,sans-serif;font-size:28px;color:var(--white)}
.field{top:400px;height:50px;background:var(--white);font-size:16px;line-height:50px;padding-left:16px;color:#333}
.field-issue{left:272px;width:332px;border-right:1px solid #ccc}
.field-city{left:605px;width:272px}
.search-btn{left:877px;top:400px;width:51px;height:50px;background:var(--orange);display:flex;align-items:center;justify-content:center}
.location{left:0;top:585px;width:1200px;height:620px;background:linear-gradient(180deg,#e6e9ed 0%,#ffffff 35%)}
.kicker{font-family:"Fjalla One",Arial,sans-serif;font-size:22px;color:var(--navy)}
.big{font-family:"Fjalla One",Arial,sans-serif;font-size:42px;color:var(--blue);line-height:1.1}
.sub{font-size:22px;color:var(--navy)}
ul.links{list-style:none}
ul.links li{font-size:13px;line-height:27.8px;color:var(--text);padding-left:18px;position:relative;white-space:nowrap}
ul.links li::before{content:"";position:absolute;left:2px;top:10px;width:6px;height:6px;border-top:2px solid var(--orange);border-right:2px solid var(--orange);transform:rotate(45deg)}
.map{left:740px;top:760px;width:400px;height:410px;background:radial-gradient(ellipse at 55% 50%,#d3d5d8 0%,#e4e6e8 60%,#ffffff 80%)}
.map-label{left:985px;top:820px;background:var(--white);border:1px solid #999;font-size:15px;padding:4px 12px}
.slant{left:0;top:1190px}
.practice{left:0;top:1228px;width:1200px;height:735px;background:linear-gradient(180deg,#eceef1 0%,#ffffff 40%)}
ul.practice-list li{font-size:17px;line-height:27.6px;padding-left:22px}
ul.practice-list li::before{top:10px}
.divider{left:0;top:1960px;width:1200px;height:2px;background:#e3e5e8}
.info-title{left:60px;top:2010px;font-family:"Fjalla One",Arial,sans-serif;font-size:42px;color:var(--blue)}
.info-sub{left:60px;top:2070px;font-size:22px;color:var(--navy)}
.feature{top:2140px;width:300px;text-align:center}
.feature .ring{width:108px;height:108px;border-radius:50%;border:3px solid var(--orange);margin:0 auto;display:flex;align-items:center;justify-content:center}
.feature h3{font-family:"Fjalla One",Arial,sans-serif;font-weight:400;font-size:21px;color:var(--navy);margin-top:36px}
.footer-strip{left:0;top:2362px;width:1200px;height:5px;background:var(--grey-line)}
.footer{left:0;top:2367px;width:1200px;height:96px;background:var(--blue);color:var(--white)}
.footer-links{left:62px;top:38px;font-size:13px;display:flex;gap:16px}
.copyright{right:62px;top:40px;font-size:11px}
</style>
</head>
<body>
<div class="abs top-strip"></div>

<header>
  <div class="abs brand">
    <div class="brand-name"><span class="dot"></span>KantoorVinder</div>
    <div class="brand-tag">YOUR PUNCH LINE GOES HERE</div>
  </div>
  <div class="abs btn btn-signin">Sign In</div>
  <div class="abs btn btn-listed">Lawyers Get Listed</div>
</header>

<nav class="abs nav">
  <ul>
    <li class="active">Home</li>
    <li>Find a Lawyer</li>
    <li>Lawyer Marketing</li>
    <li>Legal Answers</li>
    <li>More ▾</li>
  </ul>
</nav>

<section class="abs hero" role="img" aria-label="Photo of a team of lawyers meeting around a conference table in a bright office"></section>
<div class="abs search-panel"></div>
<div class="abs search-title">Let us help you find a Law Firms around the Netherlands</div>
<div class="abs field field-issue">Search Legal Issue or Law Firms</div>
<div class="abs field field-city">City Here</div>
<div class="abs search-btn">
  <svg width="26" height="26" viewBox="0 0 26 26"><circle cx="11" cy="11" r="7.5" fill="none" stroke="#fff" stroke-width="3"/><line x1="16.5" y1="16.5" x2="23" y2="23" stroke="#fff" stroke-width="4" stroke-linecap="round"/></svg>
</div>

<section class="abs location"></section>
<div class="abs kicker" style="left:60px;top:625px">Find Law Firms in</div>
<div class="abs big" style="left:60px;top:658px">Netherlands by Location</div>
<div class="abs sub" style="left:60px;top:724px">Either choose your location from the list of citys or use the map</div>

<ul class="abs links" style="left:60px;top:830px">
  <li>Almere</li><li>Amersfoort</li><li>Amsterdam</li><li>Apeldoorn</li><li>Arnhem</li><li>Beilen</li><li>Bergen Op Zoom</li><li>Bilthoven</li>
</ul>
<ul class="abs links" style="left:222px;top:830px">
  <li>Bussum</li><li>Dordrecht</li><li>Eindhoven</li><li>Enschede</li><li>Haarlem</li><li>Hilversum</li><li>Hoofddorp</li><li>Leiden</li><li>Leimuiden</li>
</ul>
<ul class="abs links" style="left:372px;top:830px">
  <li>Maastricht</li><li>Middleburg</li><li>Nieuwegein</li><li>Nijmegen</li><li>Roosendaal</li><li>Rotterdam</li><li>Schiphol</li><li>Sittard</li><li>Soest</li>
</ul>
<ul class="abs links" style="left:526px;top:834px">
  <li>The Hague</li><li>Tiel</li><li>Utrecht</li><li>Wassenaar</li><li>Zwolle</li>
</ul>

<div class="abs map" role="img" aria-label="Map of the Netherlands with its provinces, Drenthe highlighted in orange"></div>
<div class="abs map-label">Drenthe</div>

<svg class="abs slant" width="1200" height="40" viewBox="0 0 1200 40" aria-hidden="true">
  <polygon points="0,0 1200,26 1200,40 0,40" fill="#d4d7db"/>
</svg>

<section class="abs practice"></section>
<div class="abs kicker" style="left:60px;top:1272px">Find Lawyers by</div>
<div class="abs big" style="left:60px;top:1305px">Practice Area</div>

<ul class="abs links practice-list" style="left:60px;top:1388px">
  <li>Bankruptcy</li><li>Business Law</li><li>Consumer Law</li><li>Criminal Law</li><li>Divorce</li><li>DUI &amp; DWI</li><li>Employment Law</li>
</ul>
<ul class="abs links practice-list" style="left:448px;top:1388px">
  <li>Estate Planning</li><li>Family Law</li><li>Foreclosure Defense</li><li>Immigration Law</li><li>Intellectual Property</li><li>Medical Malpractice</li><li>Nursing Home Abuse &amp; Neglect</li>
</ul>
<ul class="abs links practice-list" style="left:842px;top:1388px">
  <li>Personal Injury</li><li>Probate</li><li>Products Liability</li><li>Real Estate Law</li><li>Tax Law</li><li>Traffic Tickets</li><li>Workers' Compensation</li>
</ul>

<ul class="abs links practice-list" style="left:60px;top:1594px">
  <li>Agricultural Law</li><li>Animal &amp; Dog Law</li><li>Antitrust</li><li>Appeals &amp; Appellate</li><li>Arbitration &amp; Mediation</li><li>Asbestos &amp; Mesothelioma</li><li>Broker Fraud</li><li>Civil Rights</li><li>Collections</li><li>Communications &amp; Internet Law</li><li>Construction Law</li><li>Domestic Violence</li>
</ul>
<ul class="abs links practice-list" style="left:448px;top:1594px">
  <li>Education Law</li><li>Elder Law</li><li>Energy, Oil and Gas</li><li>Entertainment &amp; Sports</li><li>Environmental Law</li><li>Gov &amp; Administrative Law</li><li>Health Care Law</li><li>Insurance Claims</li><li>Insurance Defense</li><li>International Law</li><li>Juvenile Law</li>
</ul>
<ul class="abs links practice-list" style="left:842px;top:1594px">
  <li>Landlord Tenant</li><li>Legal Malpractice</li><li>Maritime</li><li>Military Law</li><li>Municipal Law</li><li>Native American Law</li><li>Patents</li><li>Securities Law</li><li>Social Security Disability/SSI</li><li>Trademarks</li><li>White Collar Crime</li>
</ul>

<div class="abs divider"></div>

<section>
  <h2 class="abs info-title" style="font-weight:400">Free Legal Information on Kantoorvinder online</h2>
  <p class="abs info-sub">Can Help you make an educated decision when hiring an attorney</p>

  <div class="abs feature" style="left:85px">
    <div class="ring">
      <svg width="60" height="46" viewBox="0 0 60 46"><ellipse cx="22" cy="16" rx="20" ry="14" fill="#f47a20"/><polygon points="10,26 6,38 20,29" fill="#f47a20"/><ellipse cx="40" cy="24" rx="18" ry="12" fill="#f47a20" stroke="#fff" stroke-width="3"/><polygon points="48,33 54,43 40,35" fill="#f47a20"/></svg>
    </div>
    <h3>Question &amp; Answers</h3>
  </div>

  <div class="abs feature" style="left:450px">
    <div class="ring">
      <svg width="56" height="52" viewBox="0 0 56 52"><rect x="14" y="6" width="26" height="14" rx="2" transform="rotate(-40 27 13)" fill="#f47a20"/><rect x="26" y="18" width="6" height="26" transform="rotate(-40 29 31)" fill="#f47a20"/><rect x="6" y="42" width="28" height="7" rx="1" fill="#f47a20"/></svg>
    </div>
    <h3>Legal Practice Centers</h3>
  </div>

  <div class="abs feature" style="left:815px">
    <div class="ring">
      <svg width="44" height="54" viewBox="0 0 44 54"><rect x="4" y="2" width="30" height="40" rx="2" fill="none" stroke="#f47a20" stroke-width="3"/><line x1="10" y1="12" x2="28" y2="12" stroke="#f47a20" stroke-width="3"/><line x1="10" y1="20" x2="28" y2="20" stroke="#f47a20" stroke-width="3"/><line x1="10" y1="28" x2="22" y2="28" stroke="#f47a20" stroke-width="3"/><rect x="24" y="32" width="16" height="18" rx="3" fill="#f47a20"/></svg>
    </div>
    <h3>Codes, Regulation &amp; Case Law</h3>
  </div>
</section>

<div class="abs footer-strip"></div>
<footer class="abs footer">
  <div class="abs footer-links"><span>Company</span><span>|</span><span>Terms of Service</span><span>|</span><span>Privacy Policy</span><span>|</span><span>Contact Us</span></div>
  <div class="abs copyright">Copyright kantoorvinder.website All Right Reserved.</div>
</footer>
</body>
</html>
```